Visitenkarten-Design für Integratives Business Coaching
Radoslava Tzvetkorina hat sehr zuverlässig, zügig und sorgfältig gearbeitet - herzlichen Dank!!
Zielgruppe
Ich bin Henrike Wendel | Vertriebs-Pfade L.U.X. Stärke® | Gründungs- und Unternehmensberatung (ZEFO-HWK)
Integratives Business Coaching für Start Ups, Unternehmer und alle, die eine berufliche Veränderung planen und ihre Selbständigkeit erfolgreich meistern wollen!
Aufgabenstellung
Das Design der VISITENKARTE sollte dem bestehenden Design meiner aktuellen Website https://henrike-wendel.com angepasst sein, ELEGANT aussehen und SERIÖS wirken:
Schriftart: Open sans
Schriftfarben: #0b2161 blau | #a8140f rot
Farbverlauf im Logo + auf der Website:
#a8130f
#edae44
Slogan: Klarheit & Gelassenheit
Logo mit Schriftzug: siehe Upload
Profilbild: siehe Upload (das Photo muss noch gezoomt + zugeschnitten werden)

```html
<!DOCTYPE html>
<html lang="de">
<head>
<meta charset="utf-8">
<title>Visitenkarte Henrike Wendel</title>
<link rel="stylesheet" href="https://fonts.googleapis.com/css2?family=Open+Sans:wght@400;700&display=swap">
<style>
  :root {
    --grad-start: #a8130f;
    --grad-end: #edae44;
    --ink-blue: #0b2161;
    --mark-white: #ffffff;
  }
  html, body {
    margin: 0;
    padding: 0;
    width: 1200px;
    height: 772px;
    overflow: hidden;
  }
  .card {
    position: relative;
    width: 1200px;
    height: 772px;
    background: linear-gradient(90deg, var(--grad-start) 0%, var(--grad-end) 100%);
    font-family: "Open Sans", sans-serif;
    color: var(--ink-blue);
  }
  .info {
    position: absolute;
    left: 77px;
    top: 0;
  }
  .line {
    position: absolute;
    left: 0;
    white-space: nowrap;
    font-size: 29px;
    line-height: 40px;
    font-weight: 400;
    letter-spacing: 0.1px;
  }
  .name { top: 116px; font-size: 33px; font-weight: 700; }
  .company { top: 163px; }
  .email { top: 206px; }
  .phone-office { top: 248px; }
  .phone-mobile { top: 291px; }
  .divider {
    position: absolute;
    left: 0;
    width: 137px;
    height: 2px;
    background: var(--ink-blue);
  }
  .divider-1 { top: 363px; }
  .divider-2 { top: 557px; }
  .service { top: 401px; font-weight: 700; }
  .slogan { top: 444px; }
  .website { top: 487px; }
  .social-label { top: 597px; font-size: 32px; }
  .social-handle { top: 640px; }
  .brand-mark {
    position: absolute;
    left: 953px;
    top: 112px;
    width: 168px;
    height: 168px;
  }
</style>
</head>
<body>
  <div class="card">
    <div class="info">
      <div class="line name">Henrike Wendel</div>
      <div class="line company">Vertriebs-Pfade L.U.X Stärke</div>
      <div class="line email">willkommen@henrike-wendel.com</div>
      <div class="line phone-office">(+49) 89 41 72 60 38</div>
      <div class="line phone-mobile">(+49) 151 370 52 816</div>
      <div class="divider divider-1"></div>
      <div class="line service">Gründungs- und Unternehmensberatung (ZEFO-HWK)</div>
      <div class="line slogan">Klarheit &amp; Gelassenheit</div>
      <div class="line website">henrike-wendel.com</div>
      <div class="divider divider-2"></div>
      <div class="line social-label">kontaktnetz</div>
      <div class="line social-handle">@HenrikeWendelMuenchen</div>
    </div>
    <svg class="brand-mark" viewBox="0 0 168 168" aria-label="Henrike Wendel">
      <circle cx="84" cy="84" r="84" fill="var(--mark-white)"/>
      <text x="84" y="80" text-anchor="middle" font-family="Open Sans, sans-serif" font-size="19" font-weight="400" fill="#0b2161">Henrike</text>
      <text x="84" y="104" text-anchor="middle" font-family="Open Sans, sans-serif" font-size="19" font-weight="400" fill="#0b2161">Wendel</text>
    </svg>
  </div>
</body>
</html>
```